Webdesign für Birke Werkstatt
Zielgruppe
Birke Werkstatt produziert GfK Formteile und Abdeckungen
Einzelanfertigungen • Negativ - Formenbau • Prototyping • Ur-Modellbau
Formteile • Abdeckungen • Behälter • Sonderanfertigungen • Beschichtungen
Prototypen Modellbau • Anfertigung von Negativformen • Reparaturen • Fahrzeugteile
Hauptzielgruppe ist die Luftfahrtindustrie (Abdeckungen für Triebwerke)
Durch den Prototypenbau und die Einzelanfertigungen ist die Zielgruppe nicht klar zu definieren. Es werden Einzelteile jeglicher Art aus GfK hergestellt.
Dies können auch Anbauteile für PKW, Poolbeschichtungen, Teile für Boote etc sein.
Es gibt auch Kleinserien. Beispielsweise baut Birke-Werkstatt Motorhauben für Hallo-Brenner Rasenmähertrecker aus den 70er Jahren nach, die es nicht mehr zu kaufen gibt.
Aufgabenstellung
Der Designer hat alle Freiheiten. Die Seite muss natürlich responsiv funktionieren.
Außer dem Logo gibt es keine must-haves.
Schriftart aus dem Logo: EXO 2

```html
<!DOCTYPE html>
<html lang="de">
<head>
<meta charset="utf-8">
<title>Birke Werkstatt – GfK Formteile</title>
<link href="https://fonts.googleapis.com/css2?family=Exo+2:wght@400;500;600;800&display=swap" rel="stylesheet">
<style>
:root{
  --blue:#1d5b9d;
  --blue-dark:#174a82;
  --text:#333;
  --grey:#f1f1f1;
  --box:#ededed;
  --orange:#f49b00;
  --orange-light:#fdb300;
  --white:#fff;
}
*{box-sizing:border-box;margin:0;padding:0}
html,body{width:1200px;height:3478px;overflow:hidden}
body{font-family:"Exo 2",sans-serif;color:var(--text);background:var(--white);position:relative}
.abs{position:absolute}

.topnav{top:18px;right:170px;display:flex;gap:24px;font-size:15px;color:var(--blue)}
.flag{top:17px;left:1055px;width:34px;height:20px;display:flex;flex-direction:column}
.flag span{flex:1}
.brand{top:68px;left:322px}
.brand-name{font-size:66px;font-weight:800;color:var(--blue);line-height:1;letter-spacing:-1px}
.brand-tag{font-size:19px;color:#555;margin-top:8px}
.brand-mark{top:28px;left:112px;width:180px;height:180px;border-radius:50%;border:4px solid var(--blue);background:var(--white);z-index:3}

.mainnav{top:180px;left:0;width:1200px;height:52px;background:var(--blue);display:flex;padding-left:297px;font-size:16px;color:var(--white)}
.mainnav a{display:block;padding:0 26px;line-height:52px;color:inherit;text-decoration:none;border-right:1px solid rgba(255,255,255,.2)}
.mainnav a.active{background:var(--blue-dark);position:relative}
.mainnav a:last-child{border:none}

.hero{top:232px;left:0;width:1200px;height:490px;background:linear-gradient(180deg,#8ba4bd 0%,#c9d3dc 55%,#9a9a98 80%,#7c7c7a 100%)}
.hero-caption{top:266px;left:807px;width:393px;height:111px;background:rgba(255,255,255,.88);padding:20px 34px;font-size:31px;font-weight:800;color:var(--blue);line-height:1.15}
.hero-arrow{top:452px;width:62px;height:62px;background:rgba(255,255,255,.75);display:flex;align-items:center;justify-content:center}
.dropdown{top:232px;left:533px;width:259px;background:rgba(255,255,255,.95);font-size:14px;color:var(--blue);text-align:center;list-style:none}
.dropdown li{height:38px;line-height:38px;border-bottom:1px solid #c9d7e6}

.section-title{font-size:30px;font-weight:800;color:var(--blue);text-align:center}
.about-photo{top:837px;left:109px;width:452px;height:332px;background:linear-gradient(135deg,#3d73c4,#2a5db3 50%,#c5c8cc)}
.about-text{top:1192px;left:109px;width:460px;font-size:17.5px;line-height:1.42}
.feature{left:643px;width:448px;background:var(--box)}
.feature h3{display:flex;align-items:center;gap:22px;font-size:20px;font-weight:500;color:var(--blue);height:64px;padding-left:22px}
.feature p{font-size:17px;line-height:1.38;padding:0 22px;margin-bottom:26px}

.products{top:1576px;left:0;width:1200px;height:1443px;background:var(--grey)}
.card{width:288px;height:502px;background:var(--white);box-shadow:0 2px 8px rgba(0,0,0,.12);text-align:center;padding:12px}
.card .pic{height:262px}
.card h4{font-size:19px;font-weight:800;color:var(--blue);height:62px;padding-top:16px;line-height:1.25}
.card p{font-size:16.5px;line-height:1.3;height:92px;padding-top:8px}
.btn{display:inline-block;background:linear-gradient(var(--orange-light),var(--orange));color:var(--white);font-weight:800;font-size:16px;padding:4px 24px;box-shadow:0 3px 6px rgba(0,0,0,.2)}

.footer{top:3019px;left:0;width:1200px;height:459px;background:var(--blue);color:var(--white)}
.kontakt-tab{top:2973px;left:88px;width:206px;height:46px;background:var(--blue);clip-path:polygon(16px 0,100% 0,100% 100%,0 100%);color:var(--white);font-size:30px;font-weight:800;padding-left:50px;line-height:48px}
.footer-name{top:3058px;left:137px;font-size:28px;font-weight:800}
.footer-info{top:3114px;left:137px;font-size:19px;line-height:1.28}
.form-title{top:3062px;left:660px;font-size:26px;font-weight:800;color:var(--white)}
.field{left:641px;width:447px;background:var(--white);border:1px solid #ccc;color:var(--blue);font-size:16px;padding:10px 20px}
.send{top:3383px;left:969px;width:122px;height:39px;background:var(--blue-dark);color:var(--white);font-weight:800;font-size:18px;display:flex;align-items:center;justify-content:center}
</style>
</head>
<body>

<div class="abs brand-mark" aria-hidden="true"></div>
<nav class="abs topnav"><span>Impressum</span><span>AGB</span></nav>
<div class="abs flag" aria-label="Deutsch"><span style="background:#000"></span><span style="background:#d00"></span><span style="background:#fc0"></span></div>
<div class="abs brand">
  <div class="brand-name">Birke Werkstatt</div>
  <div class="brand-tag">GfK Formteile | Ur-Modellbau | Prototyping</div>
</div>

<nav class="abs mainnav">
  <a>Startseite</a><a>Über uns</a><a class="active">Produkte &amp; Dienstleistungen</a><a>Kontakt</a>
</nav>

<div class="abs hero" role="img" aria-label="Foto: Verkehrsflugzeug mit Schlepper auf dem Vorfeld"></div>
<div class="abs hero-caption">Abdeckungen für Triebwerke</div>
<div class="abs hero-arrow" style="left:0"><svg width="24" height="30"><path d="M18 3 6 15l12 12" stroke="#1d5b9d" stroke-width="5" fill="none"/></svg></div>
<div class="abs hero-arrow" style="right:0"><svg width="24" height="30"><path d="M6 3l12 12L6 27" stroke="#1d5b9d" stroke-width="5" fill="none"/></svg></div>
<ul class="abs dropdown">
  <li>Luftfahrt Formbauteile</li><li>Aufblasbare Sonderabdeckungen</li><li>Formbauteile</li><li>Ur-Modellbau</li><li>Aquarienrückwände</li><li>Dekoration &amp; Kunstfelsen</li><li>Fahrzeugteile</li><li>Prototypen Metallbau</li><li>Reparaturen</li>
</ul>

<h2 class="abs section-title" style="top:756px;left:0;width:1200px">Über uns</h2>
<div class="abs about-photo" role="img" aria-label="Foto: Triebwerk unter blauer Schutzabdeckung"></div>
<p class="abs about-text">Wir entwickeln und fertigen geometrisch anspruchsvolle Formteile von höchster Qualität. Die von uns konzipierten Verbundwerkstoffe mit ihren herausragenden Oberflächen- und Materialeigenschaften bieten konstruktive Vorteile und erweitern die gestalterischen Möglichkeiten.</p>

<div class="abs feature" style="top:837px;height:519px">
  <h3><svg width="40" height="28" viewBox="0 0 40 28"><path d="M2 8 12 2l8 5 8-5 10 6-6 10-10 8-10-8z" fill="#1d5b9d"/></svg>Kundenorientiert</h3>
  <p>Die intensive, vertrauensvolle Zusammenarbeit mit unseren Kunden ist für uns eine der wichtigsten Voraussetzungen für den gemeinsamen Erfolg. Wir bieten darum bereits im Vorfeld eines Projekts umfassende Beratung und zeigen das breit gefächerte Anwendungsspektrum von faserverstärkten Kunststoffen auf.</p>
  <p>In enger Kooperation mit Ihnen entwickeln wir unter Einbindung aller gestalterischen und technischen Gesichtspunkte maßgeschneiderte, individuelle Lösungen für Ihre Anforderungen und Anwendungen.</p>
  <p>Im Mittelpunkt unseres Handels steht dabei die technisch perfekte, schnelle und wirtschaftliche Umsetzung der Ideen und Entwürfe unserer Kunden.</p>
</div>
<div class="abs feature" style="top:1392px;height:59px">
  <h3 style="height:59px"><svg width="40" height="28" viewBox="0 0 40 28"><path d="M4 26a16 16 0 0 1 32 0" stroke="#1d5b9d" stroke-width="5" fill="none"/><path d="M20 24 28 12" stroke="#1d5b9d" stroke-width="4"/></svg>Leistungsstark</h3>
</div>

<section class="abs products">
  <h2 class="abs section-title" style="top:54px;left:0;width:1200px">Produkte &amp; Dienstleistungen</h2>
  <svg class="abs" style="top:72px;left:1006px" width="84" height="28"><path d="M9 4 2 14l7 10" stroke="#1d5b9d" stroke-width="3" fill="none"/><rect x="14" y="3" width="16" height="22" fill="#1d5b9d"/><path d="M35 4l7 10-7 10" stroke="#1d5b9d" stroke-width="3" fill="none"/><g fill="#1d5b9d"><rect x="56" y="3" width="7" height="7"/><rect x="65" y="3" width="7" height="7"/><rect x="74" y="3" width="7" height="7"/><rect x="56" y="12" width="7" height="7"/><rect x="65" y="12" width="7" height="7"/><rect x="74" y="12" width="7" height="7"/><rect x="56" y="21" width="7" height="7"/><rect x="65" y="21" width="7" height="7"/><rect x="74" y="21" width="7" height="7"/></g></svg>
</section>

<div class="abs card" style="top:1721px;left:108px"><div class="pic" role="img" aria-label="Foto: gelbe Triebwerksabdeckung" style="background:linear-gradient(135deg,#e4e33a,#b9bd2a 60%,#7d7f6a)"></div><h4>Luftfahrt Formbauteile</h4><p>Anfertigung von Triebwerkcover für jeden Triebwerktypen.</p><span class="btn">Details</span></div>
<div class="abs card" style="top:1721px;left:454px"><div class="pic" role="img" aria-label="Foto: aufblasbare graue Sonderabdeckung in der Halle" style="background:linear-gradient(135deg,#b9b9b9,#8e8e8e 60%,#6f7175)"></div><h4>Aufblasbare Sonderabdeckungen</h4><p>Anfertigung von Triebwerkcover für jeden Triebwerktypen.</p><span class="btn">Details</span></div>
<div class="abs card" style="top:1721px;left:799px"><div class="pic" role="img" aria-label="Foto: blaue ringförmige Formbauteile" style="background:linear-gradient(135deg,#3b6fd0,#2c5cc0 60%,#c9b93a)"></div><h4>Formbauteile</h4><p>Anfertigung von technischen Formbauteilen (Einzelstück oder Kleinserien).</p><span class="btn">Details</span></div>

<div class="abs card" style="top:2283px;left:108px"><div class="pic" role="img" aria-label="Foto: Aquarienrückwand mit Felsstruktur" style="background:linear-gradient(180deg,#5a5750,#6b6760 60%,#e6e3dc)"></div><h4>Aquarium Rückwände</h4><p>3D - Kunstfelsenrückwand mit echter Granitkies-Oberfläche</p><span class="btn">Details</span></div>
<div class="abs card" style="top:2283px;left:454px"><div class="pic" role="img" aria-label="Foto: Kunstfelsen-Dekoration am Pool" style="background:linear-gradient(135deg,#6f93b8,#2d67b0 50%,#9b8a5a)"></div><h4>Dekoration &amp; Kunstfelsen</h4><p>Anfertigung von Triebwerkcover für jeden Triebwerktypen.</p><span class="btn">Details</span></div>
<div class="abs card" style="top:2283px;left:799px"><div class="pic" role="img" aria-label="Foto: reparierte weiße Oberfläche" style="background:linear-gradient(135deg,#cfcfcf,#e4e4e4 60%,#b9b9b9)"></div><h4>Reperaturservice</h4><p>Anfertigung von technischen Formbauteilen (Einzelstück oder Kleinserien).</p><span class="btn">Details</span></div>

<div class="abs kontakt-tab">Kontakt</div>
<footer class="abs footer"></footer>
<div class="abs footer-name" style="color:#fff">Birke Werkstatt</div>
<address class="abs footer-info" style="font-style:normal;color:#fff">
  Geschäftsführer: M. Halden<br>Lerchenweg 14<br>31180 Giesenfeld<br><br>
  Tel.&nbsp;&nbsp;&nbsp;&nbsp;&nbsp;+49 511 / 207 41 18<br>Fax.&nbsp;&nbsp;&nbsp;&nbsp;+49 511 / 207 41 19
</address>
<div class="abs form-title">Ihre Nachricht</div>
<div class="abs field" style="top:3102px;height:44px">Name</div>
<div class="abs field" style="top:3163px;height:43px">E-Mail</div>
<div class="abs field" style="top:3225px;height:143px">Nachricht</div>
<div class="abs send">SENDEN</div>

</body>
</html>
```